Billboard design - consider what a billboard is

Design a billboard using my logo - Billboard is 6m x 3m
A Billboard is advertising for my company that is on a big sign.

Has to be clean and easy to read, and ideally highlights that we are Residential and Commercial builders.

Keep it clean and easy to read

The contact number for the board is

022 583 7092
www.harbourframeworks.co.nz
info@harbourframeworks.co.nz

Doesnt have to have all contact details if it doesnt fit

Has to catch peoples attention to contact us if they need a builder

Can you please change the sign to be all white writing, with black background ?
Updates

Please consider what a billboard is...

The design needs to be suitable for a billboard..

Target Market(s)

people driving past

Industry/Entity Type

Construction

Logo Text

Wellington Builder, website email address, contact number

Colors
0054AA
0677BA
7BADD7
CADEEF
E8F1F8

Requirements
Must have
• Easy to read
Nice to have
• easy to read, can clearly see contact details

```html
<!DOCTYPE html>
<html lang="en">
<head>
<meta charset="UTF-8">
<title>Harbour Frameworks Billboard</title>
<link href="https://fonts.googleapis.com/css2?family=Lexend:wght@400;500;700&display=swap" rel="stylesheet">
<style>
  :root {
    --page-bg: #eef1f2;
    --face-black: #0e1418;
    --band-black: #1a2a32;
    --brand-green: #5fa35a;
    --text-white: #ffffff;
  }
  * { margin: 0; padding: 0; box-sizing: border-box; }
  html, body {
    width: 1200px;
    height: 1200px;
    overflow: hidden;
    background: var(--page-bg);
    font-family: "Lexend", "Helvetica Neue", Arial, sans-serif;
  }
  .billboard {
    position: absolute;
    left: 30px;
    top: 285px;
    width: 1140px;
    height: 630px;
    background: var(--face-black);
    border-radius: 28px;
    overflow: hidden;
    box-shadow: 0 6px 24px rgba(26, 42, 50, 0.18);
  }
  .brand-area {
    position: absolute;
    left: 0;
    top: 0;
    width: 100%;
    height: 425px;
  }
  .brand-mark {
    position: absolute;
    left: 96px;
    top: 92px;
    width: 240px;
    height: 240px;
    background: var(--brand-green);
  }
  .brand-text {
    position: absolute;
    left: 400px;
    top: 72px;
    color: var(--text-white);
  }
  .brand-name {
    font-weight: 700;
    font-size: 92px;
    line-height: 1.04;
    letter-spacing: -1px;
  }
  .brand-tagline {
    margin-top: 22px;
    font-weight: 500;
    font-size: 36px;
    line-height: 1.2;
  }
  .contact-band {
    position: absolute;
    left: 0;
    bottom: 0;
    width: 100%;
    height: 205px;
    display: flex;
  }
  .contact-location {
    width: 482px;
    background: var(--band-black);
    color: var(--text-white);
    padding: 30px 0 0 64px;
  }
  .location-name {
    font-weight: 500;
    font-size: 56px;
    line-height: 1.15;
  }
  .phone-number {
    font-weight: 500;
    font-size: 62px;
    line-height: 1.2;
    letter-spacing: -1px;
  }
  .contact-online {
    flex: 1;
    background: var(--brand-green);
    color: var(--text-white);
    display: flex;
    flex-direction: column;
    justify-content: center;
    padding-left: 54px;
    gap: 18px;
  }
  .web-address, .email-address {
    font-weight: 500;
    font-size: 29px;
    line-height: 1.2;
  }
</style>
</head>
<body>
  <main class="billboard">
    <section class="brand-area">
      <div class="brand-mark"></div>
      <div class="brand-text">
        <h1 class="brand-name">Harbour<br>Frameworks</h1>
        <p class="brand-tagline">Residential &amp; Commercial Builders</p>
      </div>
    </section>
    <section class="contact-band">
      <div class="contact-location">
        <p class="location-name">Wellington.</p>
        <p class="phone-number">022 583 7092</p>
      </div>
      <div class="contact-online">
        <p class="web-address">www.harbourframeworks.co.nz</p>
        <p class="email-address">info@harbourframeworks.co.nz</p>
      </div>
    </section>
  </main>
</body>
</html>
```